Bram's limocello

Hello Artfolkly, we need a label design for Bram’s Limoncello our first product of our new distillery. We want some simple, clean, bold graphics with a contemporary look. With only three or four colors so it can be printed on a label about three and a half inches square. We admire the art of Anton Verhulst specifically his intense colors, high contrast and whimsical humor.
We are located in Eagle Colorado which is near the ski resorts of Tusk and Granite Hollow. Our target consumer is sophisticated and affluent. Limoncello is a sweet Italian lemon liqueur which is gaining popularity in American cities. We don’t have any preconceived ideas so are open to any and all design concepts.

Cheers! 514 Distillery LLC

```html
<!DOCTYPE html>
<html lang="en">
<head>
<meta charset="utf-8">
<title>Bram’s Limoncello – Label</title>
<link rel="stylesheet" href="https://fonts.googleapis.com/css2?family=Questrial&display=swap">
<style>
  :root {
    --paper: #ffffff;
    --night: #231f20;
    --lemon-yellow: #fff200;
    --peel-light: #ffe14a;
    --peel-deep: #f2a900;
    --title-white: #ffffff;
    --subtitle-grey: #a7a9ac;
  }
  html, body {
    margin: 0;
    padding: 0;
    width: 1200px;
    height: 1100px;
    overflow: hidden;
    background: var(--paper);
  }
  .canvas {
    position: relative;
    width: 1200px;
    height: 1100px;
  }
  .label {
    position: absolute;
    left: 222px;
    top: 172px;
    width: 757px;
    height: 756px;
    overflow: hidden;
    font-family: "Questrial", "Century Gothic", sans-serif;
  }
  .label-art {
    position: absolute;
    inset: 0;
    width: 757px;
    height: 756px;
  }
  .brand {
    position: absolute;
    left: 0;
    right: 0;
    text-align: center;
    margin: 0;
    line-height: 1;
    font-weight: 400;
  }
  .brand-owner {
    top: 103px;
    font-size: 84px;
    color: var(--title-white);
    letter-spacing: 2px;
  }
  .brand-product {
    top: 187px;
    font-size: 82px;
    color: var(--lemon-yellow);
    letter-spacing: 1px;
  }
  .tagline {
    position: absolute;
    left: 0;
    right: 0;
    top: 692px;
    margin: 0;
    text-align: center;
    font-size: 34px;
    line-height: 1;
    letter-spacing: 9px;
    color: var(--subtitle-grey);
    padding-left: 10px;
  }
</style>
</head>
<body>
  <div class="canvas">
    <section class="label">
      <svg class="label-art" viewBox="0 0 757 756" xmlns="http://www.w3.org/2000/svg">
        <defs>
          <radialGradient id="peel" cx="0.42" cy="0.35" r="0.7">
            <stop offset="0" stop-color="var(--peel-light)"/>
            <stop offset="1" stop-color="var(--peel-deep)"/>
          </radialGradient>
        </defs>
        <rect class="night-sky" width="757" height="756" fill="var(--night)"/>
        <path class="sunny-ground" d="M0 423 Q378 276 757 420 L757 756 L0 756 Z" fill="var(--lemon-yellow)"/>
        <ellipse cx="378" cy="606" rx="150" ry="10" fill="#b89a00" opacity="0.45"/>
        <g role="img" aria-label="Illustration of a lemon wearing a black handlebar moustache">
          <ellipse cx="372" cy="445" rx="208" ry="168" fill="url(#peel)"/>
        </g>
      </svg>
      <h1 class="brand brand-owner">BRAM’S</h1>
      <h2 class="brand brand-product">LIMONCELLO</h2>
      <p class="tagline">ITALIAN LEMON LIQUEUR</p>
    </section>
  </div>
</body>
</html>
```